Looking for a PowerPoint design for a Pharmaceutical Company

We need a PowerPoint template design to be used company-wide. We are a pharmaceutical company with 63 years of history and want to use a new template design to work more efficiently and effectively. Below are some of the things we are looking for in the new template design.

- Simple, modern, and professional

- Practical for every day use (easy to read, easy to create)

- Slides will be mainly projected or viewed on screens, but should also work fine when printed. (e.g. We do not want to use up our inks / toners printing several pages..)

- It would be great if you could provide us a list of colors that can be effectively used in the slides. (e.g. for highlighting fonts / multiple graph colors / etc.)

- Just as an FYI, our current logo image is (dark) blue. I am not uploading the logo image here because we do not want you to be limited by the current logo image. Depending on the design, we may / may not put our logo image on the slides.

Please feel free to reach out to me if you have any questions. I look forward to seeing your design. Thank you!

Target Market(s)

Pharmaceutical industry. (To be used internally and externally)

Industry/Entity Type

Pharmaceutical

Font styles to use
Sans Serif

Requirements
Must have
• Title slide, Subtitle slide, graphs, charts, tables, bullet points, and any other slide style components normally included.
Nice to have
• - As we are in the pharma industry, we want the slides to give credibility. But we do not want it look "old", "boring", or "typical". Feel free to use unique / fresh colors.
Should not have
• - TOO many colors
• - Please do not use the images on our website, which contain faces. (Any image with faces in it...) They are stock images we bought for the website, and we do not want the images on our slides. (e.g. image of running woman on the main page, image of a surgeon, image of kids playing soccer, etc.)
• - We are not looking for a design that is a modified version of our website design. We are looking for something new.

```html
<!DOCTYPE html>
<html lang="en">
<head>
<meta charset="utf-8">
<title>Corporate Presentation Template – Slide Overview</title>
<link rel="stylesheet" href="https://fonts.googleapis.com/css2?family=Titillium+Web:ital,wght@0,300;0,400;0,600;1,300;1,400&family=Open+Sans:wght@400;600&family=Noto+Sans+KR:wght@400&display=swap">
<style>
  :root{
    --board:#dcdcdc;
    --paper:#ffffff;
    --teal:#6ddfe7;
    --teal-deep:#2bbcc6;
    --teal-soft:#c8f1f4;
    --blue:#2b94d6;
    --steel:#6b8fc9;
    --violet:#7d86d6;
    --slate:#6a6c7a;
    --grey:#dedee2;
    --grey-mid:#a9a9ad;
    --ink:#4a4a55;
    --muted:#9a9aa2;
    --head-font:"Titillium Web", "Segoe UI", sans-serif;
    --body-font:"Open Sans", Arial, sans-serif;
  }
  *{box-sizing:border-box;margin:0;padding:0}
  html,body{width:1200px;height:1000px;overflow:hidden;background:var(--board)}
  body{position:relative;font-family:var(--body-font);color:var(--ink)}

  .slide{position:absolute;width:368px;height:207px;background:var(--paper);overflow:hidden}
  .col-1{left:24px}.col-2{left:416px}.col-3{left:809px}
  .row-1{top:160px}.row-2{top:397px}.row-3{top:633px}
  .slide svg.art{position:absolute;left:0;top:0;width:368px;height:207px}

  .slide-head{position:absolute;left:0;top:0;width:100%;height:56px}
  .slide-head::before{content:"";position:absolute;left:0;top:0;width:13px;height:56px;background:var(--teal-soft)}
  .slide-head h2{position:absolute;left:21px;top:8px;font-family:var(--head-font);font-weight:300;font-size:13.5px;letter-spacing:-.2px;color:var(--ink)}
  .slide-head p{position:absolute;left:21px;top:26px;font-family:var(--head-font);font-weight:300;font-size:10px;color:var(--muted)}
  .page-no{position:absolute;right:9px;top:4px;width:19px;height:20px;background:var(--blue);color:#fff;font-family:var(--head-font);font-weight:600;font-size:11px;line-height:20px;text-align:center}
  .rights{position:absolute;right:9px;top:27px;font-size:3px;color:#c9c9cf}

  .body-copy{position:absolute;font-size:5.2px;line-height:1.75;color:#666;text-align:justify}
  .caption{font-size:4.6px;line-height:1.45;color:#777;text-align:center}
  .accent-title{position:absolute;font-family:var(--head-font);font-style:italic;font-weight:400;font-size:12.5px;color:var(--blue)}

  .brand{display:flex;align-items:center;gap:4px;font-family:"Noto Sans KR",var(--head-font),sans-serif;font-size:13px;color:#fff}
  .brand-dot{width:14px;height:14px;border-radius:50%;background:#1f3f8f}

  /* cover: coffee break */
  .coffee-photo{position:absolute;inset:0;background:linear-gradient(100deg,#7e808c 0%,#6d6f7d 55%,#585a68 100%)}
  .coffee .brand{position:absolute;left:12px;top:153px}
  .coffee-title{position:absolute;left:12px;top:175px;font-family:var(--head-font);font-style:italic;font-weight:300;font-size:18px;color:var(--blue)}

  /* section break */
  .pills-photo{position:absolute;inset:0;background:linear-gradient(180deg,#52ccd4 0%,#2fbcc6 60%,#24b4be 100%)}
  .section .brand{position:absolute;left:0;right:0;top:70px;justify-content:center}
  .section-title{position:absolute;left:0;right:0;top:89px;text-align:center;font-family:var(--head-font);font-style:italic;font-weight:300;font-size:20px;color:#fff}
  .section-note{position:absolute;left:30px;right:30px;top:180px;text-align:center;font-style:italic;font-size:5.4px;line-height:1.5;color:#eafcfd}

  .legend-item{position:absolute;font-size:4.6px;line-height:1.45;color:#777;width:52px}
  .legend-item b{display:block;font-family:var(--head-font);font-weight:600;font-size:7.5px;margin-bottom:2px}

  .swatch-row{position:absolute;left:24px;display:flex;gap:5px;align-items:center;font-size:3.8px;line-height:1.4;color:#888;width:110px}
  .swatch-row i{flex:0 0 13px;height:13px}

  .map-area{position:absolute;left:60px;top:40px;width:72px;height:160px;background:#dcdcdf;border-radius:40% 45% 30% 35%}
  .percent{position:absolute;top:77px;font-family:var(--head-font);font-weight:300;font-size:21px;color:var(--blue)}

  .data-table{position:absolute;left:15px;top:59px;width:245px;border-collapse:collapse;font-size:5.6px;text-align:center;color:#666}
  .data-table th{background:var(--slate);color:#fff;font-weight:400;height:25px;border-right:1px solid #fff}
  .data-table th.year{font-family:var(--head-font);font-style:italic;font-size:8px;width:82px}
  .data-table td{height:26px;border-right:1px solid #fff;border-bottom:1px solid #fff}
  .data-table tr.odd td{background:#ececee}
  .data-table tr.even td{background:#d5eef6}
  .data-table td.label{width:82px}
</style>
</head>
<body>

<!-- Cover: coffee break -->
<section class="slide col-1 row-1 coffee">
  <div class="coffee-photo" role="img" aria-label="Muted grey photo of a coffee mug on a desk"></div>
  <svg class="art" viewBox="0 0 368 207" aria-hidden="true">
    <g fill="none" stroke="#2b94d6" stroke-width="3" stroke-linecap="round">
      <path d="M292 44h40v24a14 14 0 0 1 -14 14h-12a14 14 0 0 1 -14 -14z"/>
      <path d="M332 50h6a8 8 0 0 1 0 16h-6"/>
      <path d="M305 22q-4 4 0 8t0 8M313 18q-4 4 0 8t0 8M321 22q-4 4 0 8t0 8"/>
    </g>
  </svg>
  <div class="brand"><span class="brand-dot"></span>하람제약</div>
  <div class="coffee-title">Coffee Break</div>
</section>

<!-- 11: bar chart -->
<section class="slide col-2 row-1">
  <header class="slide-head"><h2>DATA DRIVEN SLIDE</h2><p>Subtitle Goes Here</p><span class="page-no">11</span><small class="rights">All rights reserved</small></header>
  <p class="body-copy" style="left:32px;top:70px;width:132px">At vero eos et accusamus et iusto odio dignissimos ducimus qui blanditiis praesentium voluptatum deleniti atque corrupti quos dolores et quas molestias excepturi sint occaecati cupiditate non provident, similique sunt in culpa qui officia deserunt mollitia animi, id est laborum et dolorum fuga.</p>
  <svg class="art" viewBox="0 0 368 207">
    <g font-family="Open Sans, sans-serif" font-size="5.5" fill="#999" text-anchor="end">
      <text x="201" y="68">100</text><text x="201" y="121">50</text><text x="201" y="174">0</text>
    </g>
    <line x1="205" y1="172" x2="350" y2="172" stroke="#e3e3e3" stroke-width=".6"/>
    <g fill="var(--grey)">
      <rect x="213" y="66" width="12" height="106"/><rect x="237" y="66" width="12" height="106"/>
      <rect x="261" y="66" width="12" height="106"/><rect x="285" y="66" width="12" height="106"/>
      <rect x="309" y="66" width="12" height="106"/><rect x="333" y="66" width="12" height="106"/>
    </g>
    <g fill="var(--teal)">
      <rect x="213" y="85" width="12" height="87"/><rect x="237" y="156" width="12" height="16"/>
      <rect x="261" y="145" width="12" height="27"/><rect x="285" y="92" width="12" height="80"/>
      <rect x="309" y="164" width="12" height="8"/><rect x="333" y="122" width="12" height="50"/>
    </g>
    <g font-family="Open Sans, sans-serif" font-size="5" fill="#999" text-anchor="middle">
      <text x="219" y="182">January</text><text x="243" y="182">February</text><text x="267" y="182">March</text>
      <text x="291" y="182">April</text><text x="315" y="182">June</text><text x="339" y="182">July</text>
    </g>
  </svg>
</section>

<!-- 12: donut charts -->
<section class="slide col-3 row-1">
  <header class="slide-head"><h2>DATA DRIVEN SLIDE</h2><p>Subtitle Goes Here</p><span class="page-no">12</span><small class="rights">All rights reserved</small></header>
  <svg class="art" viewBox="0 0 368 207">
    <g fill="none" stroke-width="9">
      <circle cx="67" cy="98" r="37" stroke="#e6e6ea"/>
      <circle cx="67" cy="98" r="37" stroke="var(--grey-mid)" stroke-dasharray="116 233" transform="rotate(-90 67 98)"/>
      <circle cx="184" cy="98" r="37" stroke="#e6e6ea"/>
      <circle cx="184" cy="98" r="37" stroke="var(--teal)" stroke-dasharray="198 233" transform="rotate(-55 184 98)"/>
      <circle cx="301" cy="98" r="37" stroke="#e6e6ea"/>
      <circle cx="301" cy="98" r="37" stroke="var(--violet)" stroke-dasharray="170 233" transform="rotate(-90 301 98)"/>
    </g>
    <g font-family="Titillium Web, sans-serif" font-size="12" fill="#555" text-anchor="middle">
      <text x="67" y="163">2015</text><text x="184" y="163">2016</text><text x="301" y="163">2017</text>
    </g>
  </svg>
  <p class="caption" style="position:absolute;left:27px;top:169px;width:80px">At vero eos et accusamus et iusto odio dignissimos ducimus qui blanditiis praesentium voluptatum deleniti atque .</p>
  <p class="caption" style="position:absolute;left:144px;top:169px;width:80px">At vero eos et accusamus et iusto odio dignissimos ducimus qui blanditiis praesentium voluptatum deleniti atque .</p>
  <p class="caption" style="position:absolute;left:261px;top:169px;width:80px">At vero eos et accusamus et iusto odio dignissimos ducimus qui blanditiis praesentium voluptatum deleniti atque .</p>
</section>

<!-- 13: line chart -->
<section class="slide col-1 row-2">
  <header class="slide-head"><h2>DATA DRIVEN SLIDE</h2><p>Subtitle Goes Here</p><span class="page-no">13</span><small class="rights">All rights reserved</small></header>
  <div class="legend-item" style="left:150px;top:27px"><b style="color:var(--slate)">Color 1</b>Nam libero tempore, cum soluta nobis est eligendi optio.</div>
  <div class="legend-item" style="left:220px;top:30px"><b style="color:var(--steel)">Color 2</b>Nam libero tempore, cum soluta nobis est eligendi optio.</div>
  <div class="legend-item" style="left:291px;top:30px"><b style="color:var(--teal-deep)">Color 3</b>Nam libero tempore, cum soluta nobis est eligendi optio.</div>
  <svg class="art" viewBox="0 0 368 207">
    <g stroke="#ececec" stroke-width=".5">
      <line x1="42" y1="62" x2="340" y2="62"/><line x1="42" y1="80" x2="340" y2="80"/><line x1="42" y1="98" x2="340" y2="98"/>
      <line x1="42" y1="116" x2="340" y2="116"/><line x1="42" y1="134" x2="340" y2="134"/><line x1="42" y1="152" x2="340" y2="152"/>
      <line x1="42" y1="170" x2="340" y2="170"/>
    </g>
    <g font-family="Open Sans, sans-serif" font-size="5.5" fill="#999" text-anchor="end">
      <text x="38" y="64">300</text><text x="38" y="82">250</text><text x="38" y="100">200</text><text x="38" y="118">150</text>
      <text x="38" y="136">100</text><text x="38" y="154">50</text><text x="38" y="172">0</text>
    </g>
    <g font-family="Open Sans, sans-serif" font-size="5" fill="#999" text-anchor="middle">
      <text x="45" y="190">Quarter 1</text><text x="138" y="190">Quarter 2</text><text x="231" y="190">Quarter 3</text><text x="325" y="190">Quarter 3</text>
    </g>
    <g fill="none" stroke-width="1.2">
      <path d="M45 69C76 69 107 123 138 123S200 130 231 130S294 102 325 102" stroke="var(--teal)"/>
      <path d="M45 116C76 116 107 141 138 141S200 159 231 159S294 141 325 141" stroke="var(--steel)"/>
      <path d="M45 159C76 159 107 109 138 109S200 105 231 105S294 152 325 152" stroke="var(--slate)"/>
    </g>
    <g fill="#fff" stroke-width="1">
      <g stroke="var(--teal)"><circle cx="45" cy="69" r="2"/><circle cx="138" cy="123" r="2"/><circle cx="231" cy="130" r="2"/><circle cx="325" cy="102" r="2"/></g>
      <g stroke="var(--steel)"><circle cx="45" cy="116" r="2"/><circle cx="138" cy="141" r="2"/><circle cx="231" cy="159" r="2"/><circle cx="325" cy="141" r="2"/></g>
      <g stroke="var(--slate)"><circle cx="45" cy="159" r="2"/><circle cx="138" cy="109" r="2"/><circle cx="231" cy="105" r="2"/><circle cx="325" cy="152" r="2"/></g>
    </g>
  </svg>
</section>

<!-- 14: area chart -->
<section class="slide col-2 row-2">
  <header class="slide-head"><h2>DATA DRIVEN SLIDE</h2><p>Subtitle Goes Here</p><span class="page-no">14</span><small class="rights">All rights reserved</small></header>
  <h3 class="accent-title" style="left:28px;top:74px">Data Analysis</h3>
  <p class="body-copy" style="left:24px;top:99px;width:127px">At vero eos et accusamus et iusto odio dignissimos ducimus qui blanditiis praesentium voluptatum deleniti atque corrupti quos dolores et quas molestias excepturi sint occaecati cupiditate non provident.</p>
  <div class="swatch-row" style="top:164px"><i style="background:var(--teal)"></i>Nam libero tempore, cum soluta nobis est eligendi optio.</div>
  <div class="swatch-row" style="top:182px"><i style="background:var(--slate)"></i>Nam libero tempore, cum soluta nobis est eligendi optio.</div>
  <svg class="art" viewBox="0 0 368 207">
    <g stroke="#ececec" stroke-width=".5">
      <line x1="176" y1="63" x2="360" y2="63"/><line x1="176" y1="81" x2="360" y2="81"/><line x1="176" y1="99" x2="360" y2="99"/>
      <line x1="176" y1="118" x2="360" y2="118"/><line x1="176" y1="136" x2="360" y2="136"/><line x1="176" y1="154" x2="360" y2="154"/>
      <line x1="176" y1="172" x2="360" y2="172"/><line x1="176" y1="190" x2="360" y2="190"/>
    </g>
    <g font-family="Open Sans, sans-serif" font-size="4.8" fill="#999" text-anchor="end">
      <text x="174" y="65">140</text><text x="174" y="83">120</text><text x="174" y="101">100</text><text x="174" y="120">80</text>
      <text x="174" y="138">60</text><text x="174" y="156">40</text><text x="174" y="174">20</text><text x="174" y="192">0</text>
    </g>
    <path d="M180 145L225 72L270 88L315 99L358 190H180z" fill="var(--slate)"/>
    <path d="M180 163L225 81L270 127L315 99L358 190H180z" fill="var(--teal)"/>
    <g font-family="Open Sans, sans-serif" font-size="5" fill="#999" text-anchor="middle">
      <text x="180" y="199">Quarter 1</text><text x="225" y="199">Quarter 2</text><text x="270" y="199">Quarter 3</text><text x="315" y="199">Quarter 4</text>
    </g>
  </svg>
</section>

<!-- Section break -->
<section class="slide col-3 row-2 section">
  <div class="pills-photo" role="img" aria-label="Teal-tinted close-up photo of white tablets"></div>
  <div class="brand"><span class="brand-dot"></span>하람제약</div>
  <div class="section-title">Section Break</div>
  <p class="section-note">omnis voluptas assumenda est, omnis dolor repellendus. Temporibus autem quibusdam et aut officiis debitis aut rerum necessitatibus saepe eveniet.</p>
</section>

<!-- 15: map infographics -->
<section class="slide col-1 row-3">
  <header class="slide-head"><h2>MAP INFOGRAPHICS</h2><p>Subtitle Goes Here</p><span class="page-no">15</span><small class="rights">All rights reserved</small></header>
  <div class="map-area" role="img" aria-label="Map of South Korea with regional markers"></div>
  <svg class="art" viewBox="0 0 368 207">
    <circle cx="113" cy="70" r="9" fill="var(--steel)"/>
    <circle cx="90" cy="108" r="9" fill="var(--teal)"/>
    <circle cx="126" cy="137" r="11" fill="var(--blue)"/>
    <g fill="none" stroke-width="6">
      <circle cx="224" cy="54" r="16" stroke="#e6e6ea"/>
      <circle cx="224" cy="54" r="16" stroke="var(--steel)" stroke-dasharray="47 101" transform="rotate(-90 224 54)"/>
      <circle cx="278" cy="54" r="16" stroke="#e6e6ea"/>
      <circle cx="278" cy="54" r="16" stroke="var(--teal)" stroke-dasharray="84 101" transform="rotate(-90 278 54)"/>
      <circle cx="331" cy="54" r="16" stroke="#e6e6ea"/>
      <circle cx="331" cy="54" r="16" stroke="var(--blue)" stroke-dasharray="68 101" transform="rotate(-90 331 54)"/>
    </g>
  </svg>
  <div class="percent" style="left:202px">47%</div>
  <div class="percent" style="left:256px">83%</div>
  <div class="percent" style="left:309px">67%</div>
  <p class="body-copy" style="left:201px;top:120px;width:152px;line-height:1.45">Omnis iste natus error sit voluptatem accusantium doloremque laudantium, totam rem aperiam, eaque ipsa quae ab illo inventore veritatis et quasi architecto beatae vitae dicta sunt explicabo.</p>
  <p class="body-copy" style="left:201px;top:148px;width:152px;line-height:1.45">Nemo enim ipsam voluptatem quia voluptas sit aspernatur aut odit aut fugit, sed quia consequuntur magni dolores eos qui ratione voluptatem sequi nesciunt.</p>
  <p class="body-copy" style="left:201px;top:171px;width:152px;line-height:1.45">Nam libero tempore, cum soluta nobis est eligendi optio cumque nihil impedit.</p>
</section>

<!-- 17: table -->
<section class="slide col-2 row-3">
  <header class="slide-head"><h2>TABLE SLIDE</h2><p>Subtitle Goes Here</p><span class="page-no">17</span><small class="rights">All rights reserved</small></header>
  <table class="data-table">
    <thead><tr><th class="year">2016</th><th>Data 1</th><th>Data 2</th><th>Data 3</th><th>Data 4</th></tr></thead>
    <tbody>
      <tr class="odd"><td class="label">Pharmaceutical Business</td><td>3500</td><td>4500</td><td>7500</td><td>6500</td></tr>
      <tr class="even"><td class="label">CMO Business</td><td>1500</td><td>2500</td><td>8500</td><td>9500</td></tr>
      <tr class="odd"><td class="label">Medical Device Business</td><td>4500</td><td>5500</td><td>2500</td><td>1500</td></tr>
      <tr class="even"><td class="label">Consumer Health Business</td><td>10500</td><td>3500</td><td>6500</td><td>4500</td></tr>
    </tbody>
  </table>
  <h3 class="accent-title" style="left:272px;top:106px">Data Analysis</h3>
  <p class="body-copy" style="left:272px;top:131px;width:88px;line-height:1.6">At vero eos et accusamus et iusto odio dignissimos ducimus qui blanditiis praesentium voluptatum deleniti atque corrupti quos dolores et quas molestias excepturi sint occaecati cupiditate non provident.</p>
</section>

<!-- 18: project management -->
<section class="slide col-3 row-3">
  <header class="slide-head"><h2>PROJECT MANAGEMENT SLIDE</h2><p>Subtitle Goes Here</p><span class="page-no">18</span><small class="rights">All rights reserved</small></header>
  <svg class="art" viewBox="0 0 368 207">
    <rect x="18" y="49" width="334" height="12" fill="var(--slate)"/>
    <rect x="18" y="61" width="29" height="135" fill="var(--teal)"/>
    <g stroke="#e8e8ec" stroke-width=".5">
      <line x1="47" y1="72" x2="352" y2="72"/><line x1="47" y1="84" x2="352" y2="84"/><line x1="47" y1="95" x2="352" y2="95"/>
      <line x1="47" y1="106" x2="352" y2="106"/><line x1="47" y1="117" x2="352" y2="117"/><line x1="47" y1="129" x2="352" y2="129"/>
      <line x1="47" y1="140" x2="352" y2="140"/><line x1="47" y1="151" x2="352" y2="151"/><line x1="47" y1="162" x2="352" y2="162"/>
      <line x1="47" y1="174" x2="352" y2="174"/><line x1="47" y1="185" x2="352" y2="185"/><line x1="47" y1="196" x2="352" y2="196"/>
      <line x1="57" y1="61" x2="57" y2="196"/><line x1="77" y1="61" x2="77" y2="196"/><line x1="96" y1="61" x2="96" y2="196"/>
      <line x1="116" y1="61" x2="116" y2="196"/><line x1="136" y1="61" x2="136" y2="196"/><line x1="155" y1="61" x2="155" y2="196"/>
      <line x1="175" y1="61" x2="175" y2="196"/><line x1="195" y1="61" x2="195" y2="196"/><line x1="214" y1="61" x2="214" y2="196"/>
      <line x1="234" y1="61" x2="234" y2="196"/><line x1="254" y1="61" x2="254" y2="196"/><line x1="273" y1="61" x2="273" y2="196"/>
      <line x1="293" y1="61" x2="293" y2="196"/><line x1="313" y1="61" x2="313" y2="196"/><line x1="332" y1="61" x2="332" y2="196"/>
    </g>
    <g stroke="#fff" stroke-width=".5">
      <line x1="18" y1="72" x2="47" y2="72"/><line x1="18" y1="84" x2="47" y2="84"/><line x1="18" y1="95" x2="47" y2="95"/>
      <line x1="18" y1="106" x2="47" y2="106"/><line x1="18" y1="117" x2="47" y2="117"/><line x1="18" y1="129" x2="47" y2="129"/>
      <line x1="18" y1="140" x2="47" y2="140"/><line x1="18" y1="151" x2="47" y2="151"/><line x1="18" y1="162" x2="47" y2="162"/>
      <line x1="18" y1="174" x2="47" y2="174"/><line x1="18" y1="185" x2="47" y2="185"/>
    </g>
    <text x="32" y="57.5" font-family="Titillium Web, sans-serif" font-style="italic" font-size="7" fill="#fff" text-anchor="middle">2016</text>
    <g font-family="Open Sans, sans-serif" font-size="4.6" fill="#fff" text-anchor="middle">
      <text x="52" y="57">1</text><text x="62" y="57">2</text><text x="72" y="57">3</text><text x="81" y="57">4</text><text x="91" y="57">5</text>
      <text x="101" y="57">6</text><text x="111" y="57">7</text><text x="121" y="57">8</text><text x="131" y="57">9</text><text x="140" y="57">10</text>
      <text x="150" y="57">11</text><text x="160" y="57">12</text><text x="170" y="57">13</text><text x="180" y="57">14</text><text x="190" y="57">15</text>
      <text x="199" y="57">16</text><text x="209" y="57">17</text><text x="219" y="57">18</text><text x="229" y="57">19</text><text x="239" y="57">20</text>
      <text x="249" y="57">21</text><text x="258" y="57">22</text><text x="268" y="57">23</text><text x="278" y="57">24</text><text x="288" y="57">25</text>
      <text x="298" y="57">26</text><text x="308" y="57">27</text><text x="317" y="57">28</text><text x="327" y="57">29</text><text x="337" y="57">30</text>
      <text x="347" y="57">31</text>
    </g>
    <g font-family="Open Sans, sans-serif" font-size="3.8" fill="#fff" text-anchor="middle">
      <text x="32" y="68">January</text><text x="32" y="79.5">February</text><text x="32" y="91">March</text><text x="32" y="102">April</text>
      <text x="32" y="113">May</text><text x="32" y="124.5">June</text><text x="32" y="136">July</text><text x="32" y="147">August</text>
      <text x="32" y="158">September</text><text x="32" y="169.5">October</text><text x="32" y="181">November</text><text x="32" y="192">December</text>
    </g>
    <g stroke-linecap="round" stroke-width="6">
      <line x1="60" y1="78" x2="164" y2="78" stroke="var(--steel)"/>
      <line x1="164" y1="100" x2="218" y2="100" stroke="var(--grey-mid)"/>
      <line x1="103" y1="134" x2="279" y2="134" stroke="var(--blue)"/>
      <line x1="251" y1="157" x2="318" y2="157" stroke="#bdbdc1"/>
      <line x1="173" y1="180" x2="348" y2="180" stroke="var(--teal-deep)"/>
    </g>
  </svg>
</section>

</body>
</html>
```